Ward Compass Business Card Design*

We need a business card design for our company Ward Compass. Our company is specialized in providing online consulting services regarding medical institutions, hospitals and doctors. We work with patients worldwide looking to choose between healthcare providers. We have a website you may use as a reference, where we list doctors and clinics worldwide. So we target Medical providers as well as patients worldwide.
Target Market(s)
Medical Providers and patients around the world
Industry/Entity Type
Medical
Contact Information for Business Card
Salma Driouch
CEO
+90 612 348 2751
info@wardcompass.example
www.wardcompass.example
17 Essafsaf 3 H.Q.L. Rabat, Morocco
Requirements
Must have
- Company logo/name on one full side, personal info and smaller logo and company name on the other side.
Nice to have
- Smart and elegant design

```html
<!DOCTYPE html>
<html lang="en">
<head>
<meta charset="utf-8">
<title>Ward Compass — Business Card</title>
<link href="https://fonts.googleapis.com/css2?family=Nunito+Sans:wght@300;400;700;800&display=swap" rel="stylesheet">
<style>
  :root {
    --navy: #1b4577;
    --grey: #7c7b7c;
    --ink: #4a4a4a;
    --paper: #f3f3f5;
    --backdrop: #e7e4df;
    --white: #ffffff;
  }
  * { margin: 0; padding: 0; box-sizing: border-box; }
  html, body {
    width: 900px;
    height: 1200px;
    overflow: hidden;
    background: var(--backdrop);
    font-family: "Nunito Sans", Arial, sans-serif;
  }
  .canvas { position: relative; width: 900px; height: 1200px; }

  .card {
    position: absolute;
    left: 77px;
    width: 746px;
    height: 437px;
    box-shadow: 0 4px 10px rgba(0,0,0,0.25);
  }
  .card--front { top: 134px; background: var(--paper); }
  .card--back  { top: 638px; background: var(--navy); }

  .abs { position: absolute; line-height: 1; white-space: nowrap; }

  /* Front */
  .front-wordmark {
    left: 61px; top: 72px;
    font-size: 37px; font-weight: 800;
    color: var(--navy);
    text-transform: uppercase;
    letter-spacing: 0.2px;
  }
  .front-mark {
    position: absolute;
    left: 489px; top: 130px;
    width: 160px; height: 160px;
    border-radius: 50%;
    background: var(--navy);
  }
  .person-name {
    left: 54px; top: 214px;
    font-size: 25px; text-transform: uppercase;
    color: var(--grey); font-weight: 400;
  }
  .person-name strong { color: var(--navy); font-weight: 800; }
  .person-role {
    left: 54px; top: 244px;
    font-size: 18px; color: var(--grey); font-weight: 400;
  }
  .rule {
    position: absolute; left: 54px; top: 272px;
    width: 40px; height: 1px; background: var(--grey);
  }
  .address {
    left: 54px; top: 303px;
    font-size: 18px; line-height: 23px; color: var(--ink);
  }
  .contact {
    left: 54px; font-size: 18px; color: var(--ink);
    display: flex; align-items: center; gap: 13px;
  }
  .contact--phone { top: 364px; }
  .contact--email { top: 387px; }
  .contact svg { width: 15px; height: 15px; fill: var(--navy); flex: none; }

  /* Back */
  .back-mark {
    position: absolute;
    left: 135px; top: 164px;
    width: 104px; height: 104px;
    border-radius: 50%;
    background: var(--white);
  }
  .back-wordmark {
    left: 262px; top: 200px;
    font-size: 43px; font-weight: 800;
    color: var(--white);
    text-transform: uppercase;
  }
  .website {
    left: 0; right: 0; top: 402px;
    text-align: center;
    font-size: 17px; letter-spacing: 4px;
    color: var(--white); font-weight: 400;
  }
</style>
</head>
<body>
<main class="canvas">
  <section class="card card--front" aria-label="Business card front">
    <div class="abs front-wordmark">Ward Compass</div>
    <div class="front-mark" aria-hidden="true"></div>

    <div class="abs person-name"><strong>Salma</strong> Driouch</div>
    <div class="abs person-role">CEO</div>
    <div class="rule"></div>

    <div class="abs address">17 Essafsaf 3 H.Q.L.<br>Rabat, Morocco</div>

    <div class="abs contact contact--phone">
      <svg viewBox="0 0 24 24" aria-hidden="true"><path d="M6.6 10.8c1.4 2.8 3.8 5.1 6.6 6.6l2.2-2.2c.3-.3.7-.4 1-.2 1.1.4 2.3.6 3.6.6.6 0 1 .4 1 1V20c0 .6-.4 1-1 1C10.6 21 3 13.4 3 4c0-.6.4-1 1-1h3.5c.6 0 1 .4 1 1 0 1.3.2 2.5.6 3.6.1.3 0 .7-.2 1l-2.3 2.2z"/></svg>
      <span>+90 612 348 2751</span>
    </div>
    <div class="abs contact contact--email">
      <svg viewBox="0 0 24 24" aria-hidden="true"><path d="M2 5h20v14H2V5zm2 2v.5l8 5.5 8-5.5V7H4zm0 3v7h16v-7l-8 5.5L4 10z"/></svg>
      <span>info@wardcompass.example</span>
    </div>
  </section>

  <section class="card card--back" aria-label="Business card back">
    <div class="back-mark" aria-hidden="true"></div>
    <div class="abs back-wordmark">Ward Compass</div>
    <div class="abs website">www.wardcompass.example</div>
  </section>
</main>
</body>
</html>
```